cover for CD- Single.

This design is for a CD cover. The design is at your disposal, using all of your creative talents.
Things to improve the photo: Cleaning the face, removing blemishes.
Design in black and white would be an option (Color would be another option). I reiterate it is up to your taste and criteria, any reform and art on the cover of Cd.
Name of the single: El Camino del Silencio
Artist Name: Marisol Duarte

Target Market(s)

Single Music

Industry/Entity Type

Music

Colors

Designer to choose colors to be used in the design.

Requirements
Must have
• style, elegance, professionalism, spontaneity
Nice to have
• I want it to be as professional as possible.
Should not have
• Spelling errors.

```html
<!DOCTYPE html>
<html lang="es">
<head>
<meta charset="UTF-8">
<title>El Camino del Silencio — Marisol Duarte</title>
<link rel="stylesheet" href="https://fonts.googleapis.com/css2?family=Playfair+Display:wght@700&family=Playball&family=Cinzel:wght@400&display=swap">
<style>
  :root {
    --page-bg: #ffffff;
    --frame-white: #ffffff;
    --sunset-orange: #ff7a1e;
    --sunset-red: #e8323f;
    --magenta: #9c2a5c;
    --night: #140d16;
    --photo-light: #f6e2f2;
    --photo-pink: #e9bfdc;
    --photo-mauve: #a77aa6;
    --photo-violet: #3a1a44;
    --photo-dark: #150c17;
    --gold-top: #ffc43a;
    --gold-bottom: #f25a2e;
    --script-top: #f7a13a;
    --script-bottom: #c0306a;
    --band-top: #ff5248;
    --band-bottom: #8e1f4c;
    --artist-text: #ffffff;
  }
  html, body {
    margin: 0;
    padding: 0;
    width: 720px;
    height: 1200px;
    overflow: hidden;
    background: var(--page-bg);
  }
  .stage {
    position: relative;
    width: 720px;
    height: 1200px;
  }
  .single-cover {
    position: absolute;
    left: 60px;
    top: 300px;
    width: 600px;
    height: 600px;
    display: block;
  }
  .cover-title-caps {
    font-family: "Playfair Display", "Bodoni Moda", serif;
    font-weight: 700;
  }
  .cover-title-script {
    font-family: "Playball", cursive;
  }
  .cover-artist {
    font-family: "Cinzel", serif;
    font-weight: 400;
  }
</style>
</head>
<body>
<main class="stage">
  <svg class="single-cover" viewBox="0 0 880 880" xmlns="http://www.w3.org/2000/svg">
    <defs>
      <linearGradient id="backdropGradient" x1="0" y1="0" x2="1" y2="1">
        <stop offset="0" stop-color="var(--sunset-orange)"/>
        <stop offset="0.3" stop-color="var(--sunset-red)"/>
        <stop offset="0.6" stop-color="var(--magenta)"/>
        <stop offset="1" stop-color="var(--night)"/>
      </linearGradient>
      <linearGradient id="portraitBase" x1="0" y1="0" x2="1" y2="0.6">
        <stop offset="0" stop-color="var(--sunset-orange)"/>
        <stop offset="0.12" stop-color="var(--sunset-red)"/>
        <stop offset="0.28" stop-color="var(--photo-mauve)"/>
        <stop offset="0.45" stop-color="var(--photo-pink)"/>
        <stop offset="0.72" stop-color="var(--photo-violet)"/>
        <stop offset="1" stop-color="var(--photo-dark)"/>
      </linearGradient>
      <radialGradient id="portraitGlow" cx="0.47" cy="0.42" r="0.42">
        <stop offset="0" stop-color="var(--photo-light)"/>
        <stop offset="0.6" stop-color="var(--photo-pink)" stop-opacity="0.85"/>
        <stop offset="1" stop-color="var(--photo-pink)" stop-opacity="0"/>
      </radialGradient>
      <linearGradient id="portraitShade" x1="0" y1="0" x2="0" y2="1">
        <stop offset="0.5" stop-color="var(--night)" stop-opacity="0"/>
        <stop offset="0.8" stop-color="var(--night)" stop-opacity="0.75"/>
        <stop offset="1" stop-color="var(--night)" stop-opacity="0.95"/>
      </linearGradient>
      <linearGradient id="titleGold" x1="0" y1="0" x2="0" y2="1">
        <stop offset="0" stop-color="var(--gold-top)"/>
        <stop offset="1" stop-color="var(--gold-bottom)"/>
      </linearGradient>
      <linearGradient id="titleScript" x1="0" y1="0" x2="0" y2="1">
        <stop offset="0" stop-color="var(--script-top)"/>
        <stop offset="1" stop-color="var(--script-bottom)"/>
      </linearGradient>
      <linearGradient id="bandGradient" x1="0" y1="0" x2="0" y2="1">
        <stop offset="0" stop-color="var(--band-top)"/>
        <stop offset="1" stop-color="var(--band-bottom)"/>
      </linearGradient>
    </defs>

    <rect class="cover-backdrop" x="0" y="0" width="880" height="880" fill="url(#backdropGradient)"/>

    <rect class="cover-frame" x="10" y="13" width="860" height="855" fill="var(--frame-white)"/>

    <g class="cover-portrait" role="img" aria-label="Close-up portrait of the singer with eyes closed and hand at her ear, tinted in soft pink and violet against a sunset backdrop">
      <rect x="42" y="43" width="795" height="780" fill="url(#portraitBase)"/>
      <rect x="42" y="43" width="795" height="780" fill="url(#portraitGlow)"/>
      <rect x="42" y="43" width="795" height="780" fill="url(#portraitShade)"/>
    </g>

    <polygon class="cover-band" points="0,786 880,751 880,843 0,880" fill="url(#bandGradient)"/>
    <polygon class="cover-band-edge" points="0,880 880,843 880,880" fill="var(--night)"/>

    <g class="cover-title">
      <text class="cover-title-caps" x="443" y="673" text-anchor="middle" font-size="86"
            textLength="734" lengthAdjust="spacingAndGlyphs"
            fill="var(--night)" fill-opacity="0.7">EL CAMINO DEL</text>
      <text class="cover-title-caps" x="440" y="670" text-anchor="middle" font-size="86"
            textLength="734" lengthAdjust="spacingAndGlyphs"
            fill="url(#titleGold)">EL CAMINO DEL</text>
      <text class="cover-title-script" x="443" y="760" text-anchor="middle" font-size="104"
            fill="var(--night)" fill-opacity="0.7">Silencio</text>
      <text class="cover-title-script" x="440" y="757" text-anchor="middle" font-size="104"
            fill="url(#titleScript)">Silencio</text>
    </g>

    <text class="cover-artist" x="440" y="830" text-anchor="middle" font-size="46"
          textLength="500" lengthAdjust="spacing"
          fill="var(--artist-text)">Marisol Duarte</text>
  </svg>
</main>
</body>
</html>
```